Marcus Delvane Wellness podcast

I have overcome many health challenges. All of them have put me in position to help other people do the same. Eventually I became a certified health coach through the Academy of Restorative Dietetics. I have a strong desire to help because I know what it’s like to not feel well, and do what you want. The content on this sight will equip you with the tools to live a life full of health, freedom, and happiness. Complex health topics are broken down into simple ways to understand. No wellness topic is off limits, whether its heart disease, cancer, diabetes, sleep, hormones, or any other wellness topic.

Target Market(s)

People who are interested in growth and getting healthier

Industry/Entity Type

Health and Wellness

Colors
0054AA
0677BA
7BADD7
CADEEF
E8F1F8
0094D4
00A9DD
6FCCEA
C7EBF8
E9F6FB

Requirements
Must have
• None
Nice to have
• None
Should not have
• None

```html
<!DOCTYPE html>
<html lang="en">
<head>
<meta charset="utf-8">
<title>Marcus Delvane Wellness Podcast</title>
<link rel="stylesheet" href="https://fonts.googleapis.com/css2?family=Anton&family=Oswald:wght@600&family=Sacramento&display=swap">
<style>
  :root {
    --paper: #ffffff;
    --name-blue: #6b9fc9;
    --name-dark: #2b2b2b;
    --script-blue: #6fa3d2;
    --wave-deep: #5f9dc3;
    --wave-stripe: #8fd9f9;
    --wave-fill: #7bc5e4;
    --label-white: #ffffff;
    --photo-top: #d9d5cf;
    --photo-mid: #ecebe8;
    --photo-low: #2c2c2e;
  }
  html, body {
    margin: 0;
    padding: 0;
    width: 1200px;
    height: 1200px;
    overflow: hidden;
    background: var(--paper);
  }
  .cover {
    position: relative;
    width: 1200px;
    height: 1200px;
    background: var(--paper);
    overflow: hidden;
  }
  .cover-art {
    position: absolute;
    inset: 0;
    width: 1200px;
    height: 1200px;
  }
  .first-name {
    font-family: "Anton", "Oswald", sans-serif;
    fill: var(--name-blue);
  }
  .last-name {
    font-family: "Anton", "Oswald", sans-serif;
    fill: var(--name-dark);
  }
  .show-tag {
    font-family: "Sacramento", cursive;
    fill: var(--script-blue);
  }
  .format-label {
    font-family: "Oswald", sans-serif;
    font-weight: 600;
    fill: var(--label-white);
  }
  .host-photo {
    position: absolute;
    left: 840px;
    top: 54px;
    width: 360px;
    height: 1146px;
    border-radius: 140px 140px 0 0;
    background: linear-gradient(to bottom, var(--photo-top) 0%, var(--photo-mid) 35%, var(--photo-mid) 78%, var(--photo-low) 83%, var(--photo-low) 100%);
  }
</style>
</head>
<body>
<main class="cover">
  <svg class="cover-art" viewBox="0 0 1200 1200" xmlns="http://www.w3.org/2000/svg">
    <g class="waves">
      <path fill="var(--wave-deep)" d="M0,682 C160,880 420,930 760,880 C900,860 1050,830 1200,800 L1200,1200 L0,1200 Z"/>
      <path fill="var(--wave-stripe)" d="M0,745 C170,950 440,1000 780,950 C920,930 1060,905 1200,880 L1200,1200 L0,1200 Z"/>
      <path fill="var(--wave-fill)" d="M0,762 C170,968 440,1018 780,968 C920,948 1060,923 1200,898 L1200,1200 L0,1200 Z"/>
    </g>
    <text class="first-name" x="85" y="437" font-size="392" textLength="735" lengthAdjust="spacingAndGlyphs">MARCUS</text>
    <text class="last-name" x="86" y="632" font-size="203" textLength="724" lengthAdjust="spacingAndGlyphs">DELVANE</text>
    <text class="show-tag" x="168" y="752" font-size="155" textLength="553" lengthAdjust="spacingAndGlyphs">Wellness</text>
    <text class="format-label" x="106" y="1134" font-size="52" letter-spacing="30">PODCAST</text>
  </svg>
  <div class="host-photo" role="img" aria-label="Photo of the podcast host, smiling, in a light grey t-shirt and dark trousers"></div>
</main>
</body>
</html>
```